Bref créative
Lemon Badger
Cakes and Desserts
Bright & Fun-filled
Marla Tevison
Owner
2193 Brennick Ct.
Fernwick, CO 80417
marla.tevison@postvale.net
Join us on Friendnest!
I also need stationery that ties in with my business card.
Logo for cake company

```html
<!DOCTYPE html>
<html lang="en">
<head>
<meta charset="utf-8">
<title>Lemon Badger – Business Cards</title>
<link href="https://fonts.googleapis.com/css2?family=Arimo:wght@400;700&display=swap" rel="stylesheet">
<style>
  :root {
    --pink: #e5478f;
    --pink-soft: #f3c9dc;
    --brown: #7a3710;
    --accent: #d4531f;
    --ink: #1c1c1c;
    --paper: #ffffff;
    --edge: #9a9a9a;
  }
  * { box-sizing: border-box; margin: 0; padding: 0; }
  html, body { width: 1200px; height: 708px; overflow: hidden; background: var(--paper); }
  body { position: relative; font-family: "Arimo", Arial, sans-serif; color: var(--ink); }

  .card { position: absolute; width: 582px; height: 329px; overflow: hidden; }
  .card--front { left: 31px; top: 12px; width: 552px; background: var(--paper); border: 1px solid var(--edge); }
  .card--pink { left: 595px; top: 12px; background: var(--pink); }
  .card--white { left: 31px; top: 360px; width: 552px; background: var(--paper); border: 1px solid var(--edge); }
  .card--brown { left: 595px; top: 360px; background: var(--brown); }

  .swoosh { position: absolute; top: 0; left: 0; width: 552px; height: 120px; }

  .cake-art {
    position: absolute; right: 8px; top: 84px; width: 170px; height: 245px;
    background: linear-gradient(180deg, #f8e3ec 0%, #f1ece9 60%, #f4e6ea 100%);
    border-radius: 16px 16px 0 0;
  }

  .wordmark { display: flex; align-items: center; gap: 12px; }
  .wordmark__mark { width: 22px; height: 22px; background: var(--pink); flex: none; }
  .wordmark__name { font-weight: 700; font-size: 32px; color: var(--brown); white-space: nowrap; }

  .card--front .wordmark { position: absolute; left: 18px; top: 48px; gap: 10px; }
  .card--front .wordmark__mark { width: 18px; height: 18px; }
  .card--front .wordmark__name { font-size: 26px; }

  .centered-mark { position: absolute; left: 0; right: 0; top: 146px; justify-content: center; }
  .card--pink .wordmark__name, .card--brown .wordmark__name { color: var(--paper); }
  .card--pink .wordmark__mark { background: var(--brown); }

  .holder { position: absolute; left: 210px; top: 170px; text-align: center; }
  .holder__name { font-size: 24px; color: var(--brown); }
  .holder__role { font-size: 14px; margin-top: 3px; }

  .contact { position: absolute; left: 14px; top: 228px; font-size: 15px; line-height: 19px; font-style: normal; }
  .contact__label { color: var(--accent); }

  .web { position: absolute; left: 0; right: 0; bottom: 20px; text-align: center; font-size: 17px; }
  .card--pink .web, .card--brown .web { color: var(--paper); }
</style>
</head>
<body>

<section class="card card--front">
  <svg class="swoosh" viewBox="0 0 552 120" aria-hidden="true">
    <path d="M190 0 H552 V92 C450 86 300 50 190 0 Z" fill="var(--brown)"/>
    <path d="M205 0 C310 56 440 96 552 100" fill="none" stroke="var(--pink)" stroke-width="5"/>
    <path d="M225 0 C320 48 440 84 552 88" fill="none" stroke="var(--pink-soft)" stroke-width="3"/>
  </svg>
  <div class="cake-art" role="img" aria-label="Faint tiered cake illustration"></div>
  <div class="wordmark">
    <span class="wordmark__mark"></span>
    <span class="wordmark__name">Lemon Badger</span>
  </div>
  <div class="holder">
    <p class="holder__name">Marla Tevison</p>
    <p class="holder__role">Owner</p>
  </div>
  <address class="contact">
    2193 Brennick Ct.<br>
    Fernwick, CO 80417<br>
    <span class="contact__label">Phone:</span> (415) 555-0147<br>
    <span class="contact__label">Email:</span> marla.tevison@postvale.net<br>
    <span class="contact__label">www.Join us on Friendnest!</span>
  </address>
</section>

<section class="card card--pink">
  <div class="wordmark centered-mark">
    <span class="wordmark__mark"></span>
    <span class="wordmark__name">Lemon Badger</span>
  </div>
  <p class="web">www.lemonbadgercakes.com</p>
</section>

<section class="card card--white">
  <div class="wordmark centered-mark">
    <span class="wordmark__mark"></span>
    <span class="wordmark__name">Lemon Badger</span>
  </div>
  <p class="web">www.lemonbadgercakes.com</p>
</section>

<section class="card card--brown">
  <div class="wordmark centered-mark">
    <span class="wordmark__mark"></span>
    <span class="wordmark__name">Lemon Badger</span>
  </div>
  <p class="web">www.lemonbadgercakes.com</p>
</section>

</body>
</html>
```